TALL WAVE

I am in this industry for last 15 years we have done lots of commercial site like we work with ORBEL costruction, loam properties, DRV, quill construction.
We do all domestic and commercial wall and floor tiling, swimming pools, spas, paving, marbles blue stones and muchmore.

Specializing in the wall and floor Tiling, Waterproofing and floor preparations

Industry/Entity Type

Industry

Number of Pages Required

1 page

Font styles to use
Serif
Decorative

Colors

Designer to choose colors to be used in the design.

Requirements
Must have
• domestic and commercial indoor tiling, bathroom tiling and paving pictures
Nice to have
• beautiful bathroom pictures with tile

```html
<!DOCTYPE html>
<html lang="en">
<head>
<meta charset="utf-8">
<title>TALL WAVE — Tiling Services</title>
<link href="https://fonts.googleapis.com/css2?family=Crimson+Text:wght@400;600;700&family=Berkshire+Swash&family=Dancing+Script:wght@500&display=swap" rel="stylesheet">
<style>
  :root{
    --purple:#8b72c4;
    --purple-deep:#5b3a9a;
    --red:#d9434f;
    --coral:#e85a5a;
    --ink:#2b2b2b;
    --text:#444;
    --rule:#cfcfcf;
    --grey:#f0f0f0;
    --white:#fff;
  }
  *{box-sizing:border-box;margin:0;padding:0}
  html,body{width:1176px;height:1200px;overflow:hidden;background:var(--white)}
  body{position:relative;font-family:"Crimson Text",Georgia,serif;color:var(--text)}

  .hero{position:absolute;left:0;top:0;width:1176px;height:362px;
    background:linear-gradient(90deg,#6a3aa0 0%,#a24a8e 50%,#d8404e 100%)}
  .hero-lead{position:absolute;left:0;width:1176px;top:30px;text-align:center;
    color:var(--white);font-size:16.5px;font-weight:600;line-height:29px}
  .btn{position:absolute;display:flex;align-items:center;justify-content:center;
    color:var(--white);border:2px solid var(--white);font-weight:700;font-family:"Crimson Text",serif}
  .hero-btn{left:488px;top:116px;width:216px;height:54px;border-radius:27px;font-size:15px}
  .hero-wave{position:absolute;left:0;top:0}
  .scroll-down{position:absolute;left:570px;top:308px;width:48px;height:48px;border-radius:50%;
    background:var(--purple);display:flex;align-items:center;justify-content:center}

  .section-title{position:absolute;left:0;width:1176px;text-align:center;
    font-family:"Berkshire Swash",cursive;font-size:38px;color:var(--ink);letter-spacing:1px}
  .section-title span{color:var(--coral)}
  .services-title{top:398px}
  .services-intro{position:absolute;left:220px;width:736px;top:454px;text-align:center;
    font-size:12.8px;line-height:19.5px;color:var(--text)}

  .service{position:absolute;left:112px;width:123px;border-bottom:2px solid var(--rule)}
  .service.active{border-bottom-color:var(--purple)}
  .service-icon{width:56px;height:48px;margin-left:1px}
  .service-name{font-family:"Dancing Script",cursive;font-size:18px;color:var(--ink);
    margin-top:12px;padding-bottom:12px}

  .panel{position:absolute;left:308px;top:540px;width:769px;height:479px;background:var(--purple)}
  .panel-pointer{position:absolute;left:278px;top:753px}
  .photo{position:absolute;width:153px;height:109px}
  .panel-text{position:absolute;left:371px;top:845px;width:660px;color:var(--white);
    font-size:13px;line-height:22.5px}
  .panel-btn{left:377px;top:956px;width:127px;height:33px;border-radius:17px;font-size:13px;font-weight:600}

  .about-photo{position:absolute;left:0;top:1076px;width:433px;height:124px;
    background:linear-gradient(135deg,#e48a88,#f0a79b 60%,#d9787a)}
  .about{position:absolute;left:433px;top:1076px;width:743px;height:124px;background:var(--grey)}
  .about-title{position:absolute;left:99px;top:46px;font-family:"Berkshire Swash",cursive;
    font-size:34px;color:var(--ink);letter-spacing:1px}
  .about-title span{color:var(--coral)}
  .about-text{position:absolute;left:99px;top:106px;font-size:10px;color:var(--text);white-space:nowrap}
</style>
</head>
<body>

<header class="hero">
  <p class="hero-lead">We are expert contruction engineers serving our customers for last 15 years. We work with passion, creativity and inovation<br>and have done lots of commercial sites. We work with ORBEL costruction, loam properties, DRV, quill construction.</p>
  <a class="btn hero-btn">Request a quote</a>
  <svg class="hero-wave" width="1176" height="362" viewBox="0 0 1176 362">
    <path d="M0 323 C140 296 320 292 500 318 S860 366 1000 362 S1140 349 1176 342 L1176 362 L0 362 Z" fill="#fff"/>
  </svg>
  <div class="scroll-down">
    <svg width="26" height="14" viewBox="0 0 26 14"><path d="M2 2 L13 12 L24 2" fill="none" stroke="#fff" stroke-width="2"/></svg>
  </div>
</header>

<h2 class="section-title services-title">OUR <span>SERVICES</span></h2>
<p class="services-intro">Lorem ipsum dolor sit amet, consectetur adipiscing elit. Sed at lacus sed turpis cursus convallis id non tortor. Aenean condimentum tristique ex in tincidunt. Pellentesque vel purus convallis, vulputate ante ac, pellentesque est.</p>

<div class="service" style="top:540px">
  <div class="service-icon" role="img" aria-label="Brick wall icon" style="background:linear-gradient(#d6c27a 0 45%,#b0282c 45%)"></div>
  <div class="service-name">Wall Tiling</div>
</div>
<div class="service active" style="top:658px">
  <div class="service-icon" role="img" aria-label="Parquet floor icon" style="height:56px;background:#a8622e"></div>
  <div class="service-name" style="margin-top:6px">Floor Tiling</div>
</div>
<div class="service" style="top:783px">
  <div class="service-icon" role="img" aria-label="Spray can and bricks icon" style="height:58px;background:linear-gradient(90deg,#dcc93a 0 50%,#8b72c4 50%)"></div>
  <div class="service-name" style="margin-top:14px">WaterProofing</div>
</div>
<div class="service" style="top:913px">
  <div class="service-icon" role="img" aria-label="Bricks and trowel icon" style="height:56px;background:linear-gradient(90deg,#c93a3a 0 60%,#c9c9c9 60%)"></div>
  <div class="service-name" style="margin-top:14px">Floor preparations</div>
</div>

<svg class="panel-pointer" width="30" height="52" viewBox="0 0 30 52"><path d="M30 0 L0 26 L30 52 Z" fill="#8b72c4"/></svg>
<section class="panel"></section>
<div class="photo" role="img" aria-label="Paved brick plaza with city skyline" style="left:367px;top:568px;background:linear-gradient(#7fb2d6,#b9c9d2 45%,#a0684d 55%,#8f5a45)"></div>
<div class="photo" role="img" aria-label="Hallway with timber floor" style="left:531px;top:568px;background:linear-gradient(90deg,#e9e4da,#c9b8a0 50%,#7a4a28)"></div>
<div class="photo" role="img" aria-label="Glazed office with polished floor" style="left:696px;top:568px;background:linear-gradient(#c6d5df,#9cb7a8 45%,#eef2f5)"></div>
<div class="photo" role="img" aria-label="Hand laying a floor tile" style="left:862px;top:568px;background:linear-gradient(135deg,#d8d4cc,#eeebe6 60%,#b49a86)"></div>
<div class="photo" role="img" aria-label="Brick tiled corridor" style="left:367px;top:713px;background:linear-gradient(90deg,#b4552c,#e8a060 50%,#a24a22)"></div>
<div class="photo" role="img" aria-label="Paving stones being laid" style="left:531px;top:713px;background:linear-gradient(#8b8b86,#5c5a55)"></div>
<div class="photo" role="img" aria-label="Worker on ladder at wall" style="left:696px;top:713px;background:linear-gradient(90deg,#d8d8d6,#f1ece4 50%,#c3c6c8)"></div>
<div class="photo" role="img" aria-label="Bright mall interior with glossy tiles" style="left:862px;top:713px;background:linear-gradient(#a9c6e2,#e6eef6 60%,#c9d8e6)"></div>
<p class="panel-text">Lorem ipsum dolor sit amet, consectetur adipiscing elit. Sed at lacus sed turpis cursus convallis id non tortor. Aenean condimentum tristique ex in tincidunt. Pellentesque vel purus convallis, vulputate ante ac, pellentesque est. Phasellus sed lectus neque. Aenean mauris nulla, interdum vel eros vel, rutrum imperdiet elit. In consequat tempor sollicitudin.Maecenas efficitur viverra purus, eget tristique purus condimentum ac.</p>
<a class="btn panel-btn">Request a quote</a>

<div class="about-photo" role="img" aria-label="Tiler with hard hat and tools"></div>
<section class="about">
  <h2 class="about-title">ABOUT <span>US</span></h2>
  <p class="about-text">Lorem ipsum dolor sit amet, consectetur adipiscing elit. Proin cursus ullamcorper ante, ac tempus ex viverra id. Nullam sit</p>
</section>

</body>
</html>
```